Business Card/Letterhead/Envelope design
KTL & Associates
Business Card/Letterhead/Envelope design -
Creative Brief
Professional
Gregory P. Holt
Principal
2947 Brambleton Way Suite 340 Frisco, Texas 75981
gregory@ktlva.com
www.ktlva.com
Rounded corners preferable Simple Clean Cutting Edge Front: Full Color on White background or Full Color on Black background Back: Full Color on Black background
Reversed Logo centered on the back of card w/slogan of company... Passion. Performance. Results. (Black background)

```html
<!DOCTYPE html>
<html lang="en">
<head>
<meta charset="utf-8">
<title>KTL &amp; Associates – Business Cards</title>
<link rel="stylesheet" href="https://fonts.googleapis.com/css2?family=Arimo:ital,wght@0,400;0,700;1,700&display=swap">
<style>
  :root {
    --bg: #e9e6e2;
    --card: #ffffff;
    --red: #d3151b;
    --red-dark: #a50d12;
    --ink: #3a3a3a;
    --ink-soft: #555555;
    --rule: #c9c9c9;
    --swoosh-grey: #3c3c3c;
  }
  * { box-sizing: border-box; margin: 0; padding: 0; }
  html, body { width: 1200px; height: 852px; overflow: hidden; }
  body {
    background: var(--bg);
    font-family: "Arimo", Arial, sans-serif;
    color: var(--ink);
    position: relative;
  }
  .card {
    position: absolute;
    width: 500px;
    height: 286px;
    background: var(--card);
    border-radius: 16px;
    overflow: hidden;
    box-shadow: 0 6px 18px rgba(0,0,0,.18);
  }
  .card--vertical { left: 90px; top: 120px; }
  .card--stacked { left: 610px; top: 440px; }

  .swoosh { position: absolute; left: 0; bottom: 0; width: 100%; height: 90px; display: block; }

  .logo-name {
    font-weight: 700;
    font-size: 30px;
    line-height: 1;
    color: var(--ink);
    letter-spacing: .5px;
    white-space: nowrap;
  }
  .logo-tagline {
    font-size: 12.5px;
    color: var(--ink);
    margin-top: 4px;
    white-space: nowrap;
  }
  .divider { position: absolute; width: 1px; background: var(--rule); }

  .person-name { font-style: italic; font-weight: 700; color: var(--red); font-size: 16px; }
  .person-title { font-style: italic; font-weight: 700; color: var(--red); font-size: 11px; margin-top: 3px; }
  .address { font-size: 11.5px; color: var(--ink-soft); line-height: 1.4; margin-top: 12px; }

  .contacts { list-style: none; font-size: 11.5px; color: var(--ink-soft); }
  .contacts li { display: flex; align-items: center; gap: 7px; height: 17px; }
  .contacts svg { width: 11px; height: 11px; flex: none; fill: var(--red); }

  /* card 1 layout */
  .card--vertical .logo-block { position: absolute; left: 24px; top: 118px; width: 212px; }
  .card--vertical .logo-name { font-size: 20px; letter-spacing: 0; }
  .card--vertical .logo-tagline { font-size: 10.5px; margin-top: 3px; }
  .card--vertical .divider { left: 248px; top: 30px; height: 170px; }
  .card--vertical .person-block { position: absolute; left: 262px; top: 22px; }
  .card--vertical .contacts { position: absolute; left: 262px; top: 108px; }

  /* card 2 layout */
  .card--stacked .logo-block { position: absolute; left: 40px; top: 30px; }
  .card--stacked .divider { left: 258px; top: 96px; height: 96px; }
  .card--stacked .person-block { position: absolute; left: 40px; top: 100px; }
  .card--stacked .contacts { position: absolute; left: 272px; top: 98px; }
</style>
</head>
<body>

<svg width="0" height="0" style="position:absolute" aria-hidden="true">
  <defs>
    <symbol id="icon-phone" viewBox="0 0 12 12"><path d="M2.5 1 4.5 1 5 3.5 3.8 4.5C4.5 6 6 7.5 7.5 8.2L8.5 7 11 7.5 11 9.5C11 10.5 10 11 9 11 4.5 10.5 1.5 7.5 1 3 1 2 1.5 1 2.5 1Z"/></symbol>
    <symbol id="icon-mobile" viewBox="0 0 12 12"><path d="M3.5 0.5h5a1 1 0 0 1 1 1v9a1 1 0 0 1-1 1h-5a1 1 0 0 1-1-1v-9a1 1 0 0 1 1-1Zm0.5 1.5v7h4v-7Z"/></symbol>
    <symbol id="icon-fax" viewBox="0 0 12 12"><path d="M3 1h6v3H3ZM1 5h10v5H1Zm2 2v1.5h6V7Z"/></symbol>
    <symbol id="icon-email" viewBox="0 0 12 12"><path d="M6 0.5a5.5 5.5 0 1 0 3 10.1l-.6-.9A4.4 4.4 0 1 1 10.4 6v.6c0 .6-.4 1-.9 1s-.9-.4-.9-1V3.5H7.6v.4A2.6 2.6 0 1 0 8 8.2 1.9 1.9 0 0 0 11.5 6.6V6A5.5 5.5 0 0 0 6 .5Zm0 4a1.5 1.5 0 1 1 0 3 1.5 1.5 0 0 1 0-3Z"/></symbol>
    <symbol id="icon-web" viewBox="0 0 12 12"><path d="M6 .5a5.5 5.5 0 1 0 0 11 5.5 5.5 0 0 0 0-11Zm0 1.2a4.3 4.3 0 1 1 0 8.6 4.3 4.3 0 0 1 0-8.6Zm0 1.8a2.5 2.5 0 1 0 0 5 2.5 2.5 0 0 0 0-5Z"/></symbol>
    <symbol id="swoosh-shape" viewBox="0 0 500 90" preserveAspectRatio="none">
      <path d="M0 30 C150 78 330 70 500 10 L500 22 C330 82 150 90 0 42 Z" fill="var(--swoosh-grey)"/>
      <path d="M0 48 C150 96 330 88 500 30 L500 90 L0 90 Z" fill="var(--red)"/>
      <path d="M0 70 C160 100 340 96 500 56 L500 90 L0 90 Z" fill="var(--red-dark)" opacity=".5"/>
    </symbol>
  </defs>
</svg>

<article class="card card--vertical">
  <div class="logo-block">
    <div class="logo-name">KTL &amp; ASSOCIATES</div>
    <div class="logo-tagline">Business Sales/Mergers &amp; Acquisitions</div>
  </div>
  <div class="divider"></div>
  <div class="person-block">
    <div class="person-name">Gregory P. Holt</div>
    <div class="person-title">Principal</div>
    <div class="address">2947 Brambleton Way, Suite 340<br>Frisco, Texas 75981</div>
  </div>
  <ul class="contacts">
    <li><svg><use href="#icon-phone"/></svg>555.214.3080</li>
    <li><svg><use href="#icon-mobile"/></svg>555.761.4925</li>
    <li><svg><use href="#icon-fax"/></svg>555.308.1176</li>
    <li><svg><use href="#icon-email"/></svg>gregory@ktlva.com</li>
    <li><svg><use href="#icon-web"/></svg>www.ktlva.com</li>
  </ul>
  <svg class="swoosh" aria-hidden="true"><use href="#swoosh-shape"/></svg>
</article>

<article class="card card--stacked">
  <div class="logo-block">
    <div class="logo-name">KTL &amp; ASSOCIATES</div>
    <div class="logo-tagline">Business Sales/Mergers &amp; Acquisitions</div>
  </div>
  <div class="divider"></div>
  <div class="person-block">
    <div class="person-name">Gregory P. Holt</div>
    <div class="person-title">Principal</div>
    <div class="address">2947 Brambleton Way, Suite 340<br>Frisco, Texas 75981</div>
  </div>
  <ul class="contacts">
    <li><svg><use href="#icon-phone"/></svg>555.214.3080</li>
    <li><svg><use href="#icon-mobile"/></svg>555.761.4925</li>
    <li><svg><use href="#icon-fax"/></svg>555.308.1176</li>
    <li><svg><use href="#icon-email"/></svg>gregory@ktlva.com</li>
    <li><svg><use href="#icon-web"/></svg>www.ktlva.com</li>
  </ul>
  <svg class="swoosh" aria-hidden="true"><use href="#swoosh-shape"/></svg>
</article>

</body>
</html>
```